Fresh-Up our Master Presentation

We are looking for someone who can revise our main presentation and make it more attractive. The previous layout and the slides are uploaded here and need to be revised. You are welcome to work with icons etc. here. The goal is to make it look a little more creative and modern. Brisk Otter is a company from the creative industry and therefore it would be great if it also shows this.

Target Market(s)

B2B

Industry/Entity Type

Communication and Content Creation

Font styles to use
Sans Serif

```html
<!DOCTYPE html>
<html lang="de">
<head>
<meta charset="utf-8">
<title>Brisk Otter – Master Presentation</title>
<link href="https://fonts.googleapis.com/css2?family=Saira:wght@300;400;500;600&family=Barlow:wght@400;500;600&display=swap" rel="stylesheet">
<style>
:root{
  --navy:#333a4f;
  --ink:#1f2330;
  --muted:#8a8f9c;
  --num:#b7bac3;
  --soft:#eef0f3;
  --line:#e3e6ec;
  --pink:#e8409c;
  --cyan:#1aa3e4;
  --white:#ffffff;
}
*{box-sizing:border-box;margin:0;padding:0}
html,body{width:1200px;height:2835px;overflow:hidden;background:var(--white)}
body{font-family:"Barlow",sans-serif;color:var(--ink)}
.canvas{position:relative;width:1200px;height:2835px;overflow:hidden;background:var(--white)}
.abs{position:absolute}

.masthead{position:absolute;top:118px;left:0;width:1200px;display:flex;justify-content:center;align-items:center;gap:22px}
.masthead .dot{width:104px;height:104px;border-radius:50%;background:var(--navy)}
.masthead .name{font-family:"Saira",sans-serif;font-weight:600;font-size:74px;color:var(--navy);letter-spacing:-.5px}

.slide{position:absolute;background:var(--white);overflow:hidden;box-shadow:0 6px 26px rgba(40,60,110,.13)}
.slide.big{left:85px;top:300px;width:1030px;height:580px}
.slide.sm{width:507px;height:285px}
.col-l{left:85px}.col-r{left:608px}
.r1{top:932px}.r2{top:1232px}.r3{top:1532px}.r4{top:1832px}.r5{top:2132px}.r6{top:2432px}

.brand{position:absolute;display:flex;align-items:center;gap:4px;font-family:"Saira",sans-serif;font-weight:600;color:var(--navy)}
.brand i{display:block;border-radius:50%;background:var(--navy)}
.sm .brand{top:14px;right:14px;font-size:8px}
.sm .brand i{width:9px;height:9px}
.footer{position:absolute;left:26px;bottom:10px;font-size:6px;color:var(--muted)}
.pg{position:absolute;right:14px;bottom:8px;width:11px;height:11px;border-radius:50%;background:var(--navy)}

.social{position:absolute;left:0;top:0;width:1030px;height:580px;background:var(--white)}
.social .divider{position:absolute;left:515px;top:0;width:1px;height:580px;background:var(--line)}
.social .brand{top:24px;right:26px;font-size:15px}
.social .brand i{width:18px;height:18px}
.card{position:absolute;background:var(--white);border-radius:8px;box-shadow:0 4px 16px rgba(40,60,110,.11)}
.net{position:absolute;top:22px;display:flex;align-items:center;gap:6px;font-family:"Saira",sans-serif;font-weight:500;font-size:13px;color:var(--navy)}
.net i{width:12px;height:12px;border-radius:50%;background:var(--navy);display:block}
.big-num{position:absolute;font-family:"Saira",sans-serif;font-weight:300;font-size:31px;color:var(--num);letter-spacing:.5px}
.lbl{position:absolute;font-size:12px;color:var(--ink);line-height:1.15}
.pill{position:absolute;height:18px;border-radius:9px;background:var(--soft);font-size:11px;text-align:center;line-height:18px;color:var(--ink)}
.ico{position:absolute}
.pct{position:absolute;font-family:"Saira",sans-serif;font-size:20px;font-weight:500}
.pct.f{color:var(--pink)}.pct.m{color:var(--cyan)}
.phone{position:absolute;top:45px;width:160px;height:330px;border-radius:26px;background:#1b2030;padding:6px;box-shadow:0 10px 24px rgba(20,30,60,.25)}
.phone .screen{width:100%;height:100%;border-radius:21px}
.phone .notch{position:absolute;left:52px;top:6px;width:56px;height:14px;border-radius:0 0 10px 10px;background:#1b2030}
.presence{position:absolute;left:385px;top:405px;width:260px;height:76px;background:var(--soft);text-align:center;font-family:"Saira",sans-serif}
.presence .a{font-size:24px;color:var(--ink);line-height:1;margin-top:10px}
.presence .b{font-size:38px;color:var(--num);line-height:1.05;font-weight:500}
.social .footer{left:52px;bottom:18px;font-size:13px}
.social .pgn{position:absolute;left:975px;top:540px;width:26px;height:26px;border-radius:50%;background:var(--navy);color:#fff;font-size:11px;text-align:center;line-height:26px}
.mini{position:absolute;left:0;top:0;transform:scale(.4922);transform-origin:0 0}

.h-sm{position:absolute;font-family:"Saira",sans-serif;color:var(--ink);line-height:1.1}
.p-sm{position:absolute;font-size:5.6px;line-height:1.35;color:#333}
.icon-circ{position:absolute;width:16px;height:16px;border-radius:50%;background:var(--white);box-shadow:0 2px 6px rgba(40,60,110,.18);display:flex;align-items:center;justify-content:center}
.tag{position:absolute;height:10px;border-radius:5px;border:1px solid var(--line);font-size:5px;line-height:8px;text-align:center;background:var(--white)}
.thumb{position:absolute;width:80px;border-radius:4px;background:var(--white);box-shadow:0 2px 8px rgba(40,60,110,.15);padding:3px}
.thumb .img{height:66px;border-radius:3px}
.thumb span{display:block;text-align:center;font-size:5.5px;margin-top:3px}

.price{position:absolute;left:26px;top:70px;width:180px;border-collapse:collapse;font-size:5.2px}
.price th{font-weight:600;height:22px;border-bottom:1px solid var(--line)}
.price td{height:32px;text-align:center;border-bottom:1px solid var(--line)}
.price tr:nth-child(odd) td{background:#f5f6f8}
.perk{position:absolute;left:220px;width:262px;height:34px;background:var(--white);box-shadow:0 2px 8px rgba(40,60,110,.14);border-radius:3px}
.perk .sq{position:absolute;left:0;top:0;width:34px;height:34px;background:var(--navy);display:flex;align-items:center;justify-content:center}
.perk .t{position:absolute;left:44px;top:9px;font-size:5.5px;line-height:1.3}
.perk .t b{color:var(--cyan);font-weight:500}
.contact{position:absolute;left:257px;width:228px;height:22px;border-radius:11px;background:var(--soft)}
.contact .c{position:absolute;left:0;top:0;width:22px;height:22px;border-radius:50%;background:var(--white);box-shadow:0 2px 5px rgba(40,60,110,.18);display:flex;align-items:center;justify-content:center}
.contact span{position:absolute;left:30px;top:6px;font-size:7px}
</style>
</head>
<body>
<div class="canvas">

  <header class="masthead">
    <span class="dot"></span>
    <span class="name">Brisk Otter</span>
  </header>

  <section class="slide big">
    <div class="social">
      <div class="divider"></div>
      <div class="brand"><i></i>Brisk Otter</div>

      <div class="card" style="left:52px;top:110px;width:120px;height:130px">
        <div class="net" style="left:14px"><i></i>Picta</div>
        <div class="big-num" style="left:12px;top:62px">48'700</div>
        <div class="lbl" style="left:14px;top:100px">Follower</div>
      </div>
      <div class="card" style="left:192px;top:110px;width:120px;height:130px">
        <div class="net" style="left:14px"><i></i>Facely</div>
        <div class="big-num" style="left:12px;top:62px">29'200</div>
        <div class="lbl" style="left:14px;top:100px">Follower</div>
      </div>
      <div class="card" style="left:52px;top:250px;width:260px;height:130px">
        <svg class="ico" style="left:14px;top:16px" width="30" height="28" viewBox="0 0 30 28"><rect x="2" y="8" width="10" height="18" rx="2" fill="var(--navy)"/><rect x="12" y="2" width="16" height="10" rx="3" fill="var(--cyan)"/><path d="M15 12l-3 4v-4z" fill="var(--cyan)"/></svg>
        <div class="lbl" style="left:14px;top:56px">Posts zu den Themen</div>
        <div class="pill" style="left:14px;top:78px;width:106px">Unterhaltung</div>
        <div class="pill" style="left:134px;top:78px;width:106px">Sport</div>
        <div class="pill" style="left:14px;top:102px;width:226px">Familie</div>
      </div>
      <div class="card" style="left:52px;top:390px;width:120px;height:130px">
        <svg class="ico" style="left:14px;top:16px" width="24" height="22" viewBox="0 0 24 22"><rect x="0" y="0" width="3" height="22" fill="var(--navy)"/><rect x="4" y="3" width="10" height="3" fill="var(--navy)"/><rect x="4" y="9" width="14" height="3" fill="var(--navy)"/><rect x="4" y="15" width="20" height="3" fill="var(--navy)"/></svg>
        <div class="big-num" style="left:12px;top:44px">78'900</div>
        <div class="lbl" style="left:14px;top:82px;font-size:11px">Auf Picta<br>erreichte Konten pro<br>Monat</div>
      </div>
      <div class="card" style="left:192px;top:390px;width:193px;height:130px">
        <svg class="ico" style="left:14px;top:16px" width="28" height="20" viewBox="0 0 28 20"><circle cx="5" cy="4" r="3" fill="var(--cyan)"/><rect x="2" y="8" width="6" height="12" rx="2" fill="var(--cyan)"/><circle cx="14" cy="3" r="3" fill="var(--navy)"/><rect x="11" y="7" width="6" height="13" rx="2" fill="var(--navy)"/><circle cx="23" cy="4" r="3" fill="var(--cyan)"/><rect x="20" y="8" width="6" height="12" rx="2" fill="var(--cyan)"/></svg>
        <svg class="ico" style="left:12px;top:48px" width="36" height="36" viewBox="0 0 36 36"><circle cx="18" cy="18" r="13" fill="none" stroke="var(--soft)" stroke-width="6"/><circle cx="18" cy="18" r="13" fill="none" stroke="var(--pink)" stroke-width="6" stroke-dasharray="43.3 81.7" transform="rotate(-90 18 18)"/></svg>
        <div class="pct f" style="left:52px;top:46px">53%</div>
        <div class="lbl" style="left:54px;top:72px">Frauen</div>
        <svg class="ico" style="left:102px;top:48px" width="36" height="36" viewBox="0 0 36 36"><circle cx="18" cy="18" r="13" fill="none" stroke="var(--soft)" stroke-width="6"/><circle cx="18" cy="18" r="13" fill="none" stroke="var(--cyan)" stroke-width="6" stroke-dasharray="37.6 81.7" transform="rotate(-90 18 18)"/></svg>
        <div class="pct m" style="left:142px;top:46px">46%</div>
        <div class="lbl" style="left:140px;top:72px">Männer</div>
        <div class="lbl" style="left:14px;top:104px">Erreichte Zielgruppe</div>
      </div>

      <div class="phone" style="left:340px"><div class="screen" role="img" aria-label="Portrait of the first host in an orange jacket" style="background:linear-gradient(170deg,#8a8378,#c4893c 60%,#a86b2a)"></div><div class="notch"></div></div>
      <div class="phone" style="left:530px"><div class="screen" role="img" aria-label="Portrait of the second host in a dark hooded jacket" style="background:linear-gradient(170deg,#6b5a4c,#3a3a3e 55%,#8d9096)"></div><div class="notch"></div></div>

      <div class="presence"><div class="a">Social Media</div><div class="b">Präsenz</div></div>

      <div class="card" style="left:625px;top:390px;width:193px;height:130px">
        <svg class="ico" style="left:151px;top:16px" width="28" height="20" viewBox="0 0 28 20"><circle cx="5" cy="4" r="3" fill="var(--cyan)"/><rect x="2" y="8" width="6" height="12" rx="2" fill="var(--cyan)"/><circle cx="14" cy="3" r="3" fill="var(--navy)"/><rect x="11" y="7" width="6" height="13" rx="2" fill="var(--navy)"/><circle cx="23" cy="4" r="3" fill="var(--cyan)"/><rect x="20" y="8" width="6" height="12" rx="2" fill="var(--cyan)"/></svg>
        <div class="pct m" style="left:18px;top:46px">43%</div>
        <div class="lbl" style="left:20px;top:72px">Männer</div>
        <svg class="ico" style="left:58px;top:48px" width="36" height="36" viewBox="0 0 36 36"><circle cx="18" cy="18" r="13" fill="none" stroke="var(--soft)" stroke-width="6"/><circle cx="18" cy="18" r="13" fill="none" stroke="var(--cyan)" stroke-width="6" stroke-dasharray="35.1 81.7" transform="rotate(-90 18 18)"/></svg>
        <div class="pct f" style="left:104px;top:46px">56%</div>
        <div class="lbl" style="left:106px;top:72px">Frauen</div>
        <svg class="ico" style="left:144px;top:48px" width="36" height="36" viewBox="0 0 36 36"><circle cx="18" cy="18" r="13" fill="none" stroke="var(--soft)" stroke-width="6"/><circle cx="18" cy="18" r="13" fill="none" stroke="var(--pink)" stroke-width="6" stroke-dasharray="45.8 81.7" transform="rotate(-90 18 18)"/></svg>
        <div class="lbl" style="right:14px;top:104px">Erreichte Zielgruppe</div>
      </div>
      <div class="card" style="left:705px;top:110px;width:120px;height:130px">
        <div class="net" style="right:14px"><i></i>Facely</div>
        <div class="big-num" style="right:12px;top:62px">29'200</div>
        <div class="lbl" style="right:14px;top:100px">Follower</div>
      </div>
      <div class="card" style="left:845px;top:110px;width:120px;height:130px">
        <div class="net" style="right:14px"><i></i>Picta</div>
        <div class="big-num" style="right:12px;top:62px">63'700</div>
        <div class="lbl" style="right:14px;top:100px">Follower</div>
      </div>
      <div class="card" style="left:705px;top:250px;width:260px;height:130px">
        <svg class="ico" style="right:14px;top:16px" width="30" height="28" viewBox="0 0 30 28"><rect x="2" y="8" width="10" height="18" rx="2" fill="var(--navy)"/><rect x="12" y="2" width="16" height="10" rx="3" fill="var(--cyan)"/><path d="M15 12l-3 4v-4z" fill="var(--cyan)"/></svg>
        <div class="lbl" style="right:14px;top:56px">Posts zu den Themen</div>
        <div class="pill" style="left:20px;top:78px;width:106px">Unterhaltung</div>
        <div class="pill" style="left:140px;top:78px;width:106px">Sport</div>
        <div class="pill" style="left:20px;top:102px;width:226px">Motorrad</div>
      </div>
      <div class="card" style="left:845px;top:390px;width:120px;height:130px">
        <svg class="ico" style="right:14px;top:16px" width="24" height="22" viewBox="0 0 24 22"><rect x="0" y="0" width="3" height="22" fill="var(--navy)"/><rect x="4" y="3" width="10" height="3" fill="var(--navy)"/><rect x="4" y="9" width="14" height="3" fill="var(--navy)"/><rect x="4" y="15" width="20" height="3" fill="var(--navy)"/></svg>
        <div class="big-num" style="right:12px;top:44px">140'600</div>
        <div class="lbl" style="right:14px;top:82px;font-size:11px;text-align:right">Auf Picta<br>erreichte Konten pro<br>Monat</div>
      </div>

      <div class="footer">Your footer goes here</div>
      <div class="pgn">4</div>
    </div>
  </section>

  <section class="slide sm col-l r1">
    <div class="p-sm" style="left:26px;top:26px">Bern, 13. April 2023</div>
    <div class="h-sm" style="left:26px;top:130px;font-size:22px;width:270px">(Titel individuell je nach Kunde)</div>
    <div class="abs" style="left:0;top:188px;width:307px;height:1px;background:var(--line)"></div>
    <div class="p-sm" style="left:26px;top:202px;font-size:8px">Your subtitle goes here</div>
    <div class="abs" role="img" aria-label="Radio studio with microphones and a mixing desk" style="left:307px;top:0;width:200px;height:285px;background:linear-gradient(160deg,#5e636c,#2a2d33 60%,#15171b)"></div>
    <div class="brand" style="color:#fff"><i style="background:#fff"></i>Brisk Otter</div>
  </section>

  <section class="slide sm col-r r1">
    <div class="brand"><i></i>Brisk Otter</div>
    <div class="h-sm" style="left:26px;top:28px;font-size:15px">Jonas Keller und Marco Brandt</div>
    <div class="abs" role="img" aria-label="Both hosts standing in front of a city skyline" style="left:26px;top:75px;width:145px;height:182px;background:linear-gradient(180deg,#9fb0c4,#b6aea4 50%,#3d4048)"></div>
    <svg class="abs" style="left:212px;top:74px" width="270" height="16" viewBox="0 0 270 16"><circle cx="10" cy="8" r="5" fill="var(--navy)"/><circle cx="85" cy="8" r="5" fill="var(--navy)"/><circle cx="160" cy="8" r="5" fill="var(--navy)"/><circle cx="245" cy="8" r="5" fill="var(--navy)"/></svg>
    <div class="tag" style="left:184px;top:95px;width:82px">Moderatoren</div>
    <div class="tag" style="left:268px;top:95px;width:64px">Podcaster</div>
    <div class="tag" style="left:334px;top:95px;width:84px">Social Media Hosts</div>
    <div class="tag" style="left:420px;top:95px;width:62px">DJs</div>
    <div class="h-sm" style="left:184px;top:114px;font-size:10px"><b style="font-weight:600">Jonas Keller</b> und <b style="font-weight:600">Marco Brandt</b></div>
    <div class="p-sm" style="left:184px;top:127px">sind schweizweit bekannte Persönlichkeiten mit hohem Unterhaltungswert.</div>
    <div class="abs" style="left:184px;top:142px;width:298px;height:1px;background:var(--line)"></div>
    <div class="icon-circ" style="left:186px;top:165px"><svg width="8" height="8"><rect x="3" y="0" width="2" height="8" fill="var(--navy)"/></svg></div>
    <div class="p-sm" style="left:210px;top:163px;width:270px">Jonas Keller moderiert seit 20 Jahren und Marco Brandt seit 10 Jahren Morgensendungen, insbesondere von Radio Pulse in der Schweiz.</div>
    <div class="abs" style="left:184px;top:190px;width:298px;height:1px;background:var(--line)"></div>
    <div class="icon-circ" style="left:186px;top:214px"><svg width="8" height="8"><circle cx="4" cy="3" r="2" fill="var(--navy)"/><rect x="1" y="5" width="6" height="3" fill="var(--navy)"/></svg></div>
    <div class="p-sm" style="left:210px;top:206px;width:270px">Als Morgenduo «Keller und Brandt», mit dem Podcast «Die Plauderstunde» und mit verschiedenen Social Media-Formaten wie «Endlich Freitag, wenn...» haben sie sich eine grosse Community aufgebaut.</div>
    <div class="footer">Your footer goes here</div><div class="pg"></div>
  </section>

  <section class="slide sm col-l r2">
    <div class="brand"><i></i>Brisk Otter</div>
    <div class="h-sm" style="left:26px;top:72px;font-size:20px">Die<br>Community</div>
    <div class="abs" style="left:0;top:140px;width:185px;height:92px;background:var(--soft)"></div>
    <div class="abs" style="left:88px;top:138px;width:96px;height:96px;border-radius:50%;background:#d9dce2"></div>
    <div class="thumb" style="left:204px;top:45px"><div class="img" role="img" aria-label="Radio show promo poster" style="background:linear-gradient(160deg,#c0392b,#6a4a3a)"></div><span>Radio</span></div>
    <div class="thumb" style="left:304px;top:45px"><div class="img" role="img" aria-label="Illustrated podcast cover with both hosts" style="background:linear-gradient(160deg,#f2efe9,#c9a98c)"></div><span>Podcast</span></div>
    <div class="thumb" style="left:404px;top:45px"><div class="img" role="img" aria-label="Group photo of fans" style="background:linear-gradient(160deg,#8a5b4a,#3b3532)"></div><span>Social Media</span></div>
    <div class="thumb" style="left:204px;top:155px"><div class="img" role="img" aria-label="Live moderation on a stage" style="background:linear-gradient(160deg,#2f7fd0,#1b2a55)"></div><span>Live-Moderation</span></div>
    <div class="thumb" style="left:304px;top:155px"><div class="img" role="img" aria-label="DJ performance in a club" style="background:linear-gradient(160deg,#3a4a6a,#0f1320)"></div><span>DJ-Auftritte</span></div>
    <div class="thumb" style="left:404px;top:155px"><div class="img" role="img" aria-label="TV show stage with audience" style="background:linear-gradient(160deg,#3d6fd8,#1c2f7a)"></div><span>TV-Moderation</span></div>
    <div class="footer">Your footer goes here</div><div class="pg"></div>
  </section>

  <section class="slide sm col-r r2">
    <div class="mini">
      <div class="social">
        <div class="divider"></div>
        <div class="brand"><i></i>Brisk Otter</div>
        <div class="card" style="left:52px;top:110px;width:120px;height:130px"><div class="net" style="left:14px"><i></i>Picta</div><div class="big-num" style="left:12px;top:62px">48'700</div><div class="lbl" style="left:14px;top:100px">Follower</div></div>
        <div class="card" style="left:192px;top:110px;width:120px;height:130px"><div class="net" style="left:14px"><i></i>Facely</div><div class="big-num" style="left:12px;top:62px">29'200</div><div class="lbl" style="left:14px;top:100px">Follower</div></div>
        <div class="card" style="left:52px;top:250px;width:260px;height:130px"><div class="lbl" style="left:14px;top:56px">Posts zu den Themen</div><div class="pill" style="left:14px;top:78px;width:106px">Unterhaltung</div><div class="pill" style="left:134px;top:78px;width:106px">Sport</div><div class="pill" style="left:14px;top:102px;width:226px">Familie</div></div>
        <div class="card" style="left:52px;top:390px;width:120px;height:130px"><div class="big-num" style="left:12px;top:44px">78'900</div><div class="lbl" style="left:14px;top:82px;font-size:11px">Auf Picta<br>erreichte Konten pro<br>Monat</div></div>
        <div class="card" style="left:192px;top:390px;width:193px;height:130px"><div class="pct f" style="left:52px;top:46px">53%</div><div class="lbl" style="left:54px;top:72px">Frauen</div><div class="pct m" style="left:142px;top:46px">46%</div><div class="lbl" style="left:140px;top:72px">Männer</div><div class="lbl" style="left:14px;top:104px">Erreichte Zielgruppe</div></div>
        <div class="phone" style="left:340px"><div class="screen" role="img" aria-label="Portrait of the first host" style="background:linear-gradient(170deg,#8a8378,#c4893c 60%,#a86b2a)"></div><div class="notch"></div></div>
        <div class="phone" style="left:530px"><div class="screen" role="img" aria-label="Portrait of the second host" style="background:linear-gradient(170deg,#6b5a4c,#3a3a3e 55%,#8d9096)"></div><div class="notch"></div></div>
        <div class="presence"><div class="a">Social Media</div><div class="b">Präsenz</div></div>
        <div class="card" style="left:625px;top:390px;width:193px;height:130px"><div class="pct m" style="left:18px;top:46px">43%</div><div class="lbl" style="left:20px;top:72px">Männer</div><div class="pct f" style="left:104px;top:46px">56%</div><div class="lbl" style="left:106px;top:72px">Frauen</div><div class="lbl" style="right:14px;top:104px">Erreichte Zielgruppe</div></div>
        <div class="card" style="left:705px;top:110px;width:120px;height:130px"><div class="net" style="right:14px"><i></i>Facely</div><div class="big-num" style="right:12px;top:62px">29'200</div><div class="lbl" style="right:14px;top:100px">Follower</div></div>
        <div class="card" style="left:845px;top:110px;width:120px;height:130px"><div class="net" style="right:14px"><i></i>Picta</div><div class="big-num" style="right:12px;top:62px">63'700</div><div class="lbl" style="right:14px;top:100px">Follower</div></div>
        <div class="card" style="left:705px;top:250px;width:260px;height:130px"><div class="lbl" style="right:14px;top:56px">Posts zu den Themen</div><div class="pill" style="left:20px;top:78px;width:106px">Unterhaltung</div><div class="pill" style="left:140px;top:78px;width:106px">Sport</div><div class="pill" style="left:20px;top:102px;width:226px">Motorrad</div></div>
        <div class="card" style="left:845px;top:390px;width:120px;height:130px"><div class="big-num" style="right:12px;top:44px">140'600</div><div class="lbl" style="right:14px;top:82px;font-size:11px;text-align:right">Auf Picta<br>erreichte Konten pro<br>Monat</div></div>
        <div class="footer">Your footer goes here</div>
        <div class="pgn">5</div>
      </div>
    </div>
  </section>

  <section class="slide sm col-l r3">
    <div class="brand"><i></i>Brisk Otter</div>
    <div class="abs" role="img" aria-label="Podcast live show stage in blue light" style="left:0;top:53px;width:485px;height:205px;background:linear-gradient(120deg,#1e2a48,#24365e 55%,#3a5f9a)"></div>
    <svg class="abs" style="left:26px;top:72px" width="440" height="22" viewBox="0 0 440 22"><circle cx="11" cy="11" r="10" fill="#fff"/><g fill="none" stroke="#fff" stroke-width="2"><path d="M100 4a10 10 0 0 0 0 14M106 7a5 5 0 0 0 0 8M118 4a10 10 0 0 1 0 14M112 7a5 5 0 0 1 0 8"/><circle cx="186" cy="11" r="9"/><circle cx="186" cy="11" r="4"/></g><circle cx="109" cy="11" r="2" fill="#fff"/><path d="M278 2l3 6 6 1-4 4 1 6-6-3-6 3 1-6-4-4 6-1z" fill="#fff"/><circle cx="350" cy="5" r="3" fill="#fff"/><circle cx="362" cy="4" r="3" fill="#fff"/><circle cx="374" cy="5" r="3" fill="#fff"/><rect x="347" y="10" width="6" height="12" fill="#fff"/><rect x="359" y="9" width="6" height="13" fill="#fff"/><rect x="371" y="10" width="6" height="12" fill="#fff"/></svg>
    <div class="abs" style="left:26px;top:100px;width:440px;display:flex;gap:10px;color:#fff">
      <div style="width:80px"><div style="font-size:7.5px;font-weight:500;line-height:1.2">Top 10-Podcasts auf Streamly</div><div style="font-size:4.6px;line-height:1.35;margin-top:6px;opacity:.8">«Die Plauderstunde» gehört zu den Top 10-Podcasts auf Streamly und ist der erfolgreichste Comedy Podcast der Schweiz.</div></div>
      <div style="width:80px"><div style="font-size:7.5px;font-weight:500;line-height:1.2">8 Millionen<br>Mal gestreamt.</div><div style="font-size:4.6px;line-height:1.35;margin-top:6px;opacity:.8">Seit 2019 sind über 200 Folgen des Podcasts erschienen. Sie wurden über 8 Millionen Mal gestreamt.</div></div>
      <div style="width:80px"><div style="font-size:7.5px;font-weight:500;line-height:1.2">50'000<br>Menschen</div><div style="font-size:4.6px;line-height:1.35;margin-top:6px;opacity:.8">Jede Folge wird von durchschnittlich 50'000 Menschen angehört!</div></div>
      <div style="width:80px"><div style="font-size:7.5px;font-weight:500;line-height:1.2">1'200<br>Stündeler*innen</div><div style="font-size:4.6px;line-height:1.35;margin-top:6px;opacity:.8">Der Podcast wurde bereits zwei Mal live vor jeweils 1'200 Fans aufgezeichnet. Beide Shows waren in wenigen Sekunden restlos ausverkauft.</div></div>
      <div style="width:80px"><div style="font-size:7.5px;font-weight:500;line-height:1.2">24'000<br>Abonnent*innen</div><div style="font-size:4.6px;line-height:1.35;margin-top:6px;opacity:.8">Zum Podcast gehört eine Picta Seite mit fast 24'000 Abonnent*innen.</div></div>
    </div>
    <div class="h-sm" style="left:26px;top:220px;font-size:22px;color:#fff;font-weight:500">Der Podcast</div>
    <div class="footer">Your footer goes here</div><div class="pg"></div>
  </section>

  <section class="slide sm col-r r3">
    <div class="brand"><i></i>Brisk Otter</div>
    <div class="h-sm" style="left:26px;top:28px;font-size:15px">ClipTube-Content</div>
    <div class="abs" role="img" aria-label="Video thumbnail of friends jumping into a pool" style="left:0;top:93px;width:150px;height:98px;background:linear-gradient(180deg,#7fb8e6,#2f86c8 60%,#1a5f9a)"></div>
    <div class="abs" role="img" aria-label="Video thumbnail of a dialect comedy series" style="left:370px;top:93px;width:137px;height:98px;background:linear-gradient(180deg,#1a1a1a,#3a3a3a 60%,#111)"></div>
    <div class="abs" style="left:145px;top:60px;width:224px;height:140px;border-radius:6px;background:#1b1d22;padding:5px"><div role="img" aria-label="Video still of both hosts reacting in a studio" style="width:100%;height:100%;border-radius:3px;background:linear-gradient(160deg,#8d8a86,#c9b9a0 50%,#5a5048)"></div></div>
    <div class="abs" style="left:125px;top:200px;width:264px;height:6px;border-radius:0 0 8px 8px;background:#9aa0aa"></div>
    <div class="p-sm" style="left:26px;top:222px;width:455px;text-align:center">Seit vielen Jahren sind Jonas Keller und Marco Brandt mit höchst erfolgreichen ClipTube-Formaten wie «Endlich Freitag, wenn...», «Beni &amp; Fabi» oder «Dialekt für Einsteiger» präsent. Ihr Kanal hat über 17'000 Abonnent*innen! Jonas Keller und Marco Brandt gewannen 2022 zusammen mit dem Social Team von Radio Pulse den «Alpine Comedy Award».</div>
    <div class="footer">Your footer goes here</div><div class="pg"></div>
  </section>

  <section class="slide sm col-l r4">
    <div class="brand"><i></i>Brisk Otter</div>
    <div class="abs" role="img" aria-label="Concert stage with flames and crowd" style="left:0;top:0;width:245px;height:260px;background:linear-gradient(170deg,#2a1e3e,#5a2a4a 45%,#c0542a 75%,#1c1420)"></div>
    <div class="h-sm" style="left:270px;top:32px;font-size:19px">Moderationen<br>und DJ-Auftritte</div>
    <div class="icon-circ" style="left:232px;top:96px;width:22px;height:22px"><svg width="10" height="10"><circle cx="5" cy="5" r="4" fill="var(--navy)"/></svg></div>
    <div class="p-sm" style="left:270px;top:93px;width:215px">Jonas Keller und Marco Brandt sind jedes Jahr an unzähligen Events als DJs und / oder Moderatoren präsent. Sie profitieren hierbei von ihrer langen Erfahrung als Radio und TV-Moderatoren.</div>
    <div class="icon-circ" style="left:232px;top:158px;width:22px;height:22px"><svg width="10" height="10"><circle cx="5" cy="2" r="2" fill="var(--navy)"/><rect x="3" y="4" width="4" height="6" fill="var(--navy)"/></svg></div>
    <div class="p-sm" style="left:270px;top:160px;width:215px">Auch im Rahmen der Pulse Events treten Jonas Keller und Marco Brandt regelmässig vor bis zu 50'000 Menschen auf.</div>
    <div class="icon-circ" style="left:232px;top:210px;width:22px;height:22px"><svg width="10" height="10"><circle cx="5" cy="5" r="4" fill="none" stroke="var(--navy)" stroke-width="2"/></svg></div>
    <div class="p-sm" style="left:270px;top:208px;width:215px">Als DJs spielen Sie ein breites Hit-Repertoire. Sie präsentieren eigene Partyserien wie zum Beispiel in Kooperation mit Pulse im «Saalhaus Bern» und im «Kellerbar in Thun».</div>
    <div class="footer">Your footer goes here</div><div class="pg"></div>
  </section>

  <section class="slide sm col-r r4">
    <div class="brand"><i></i>Brisk Otter</div>
    <div class="h-sm" style="left:8px;top:258px;font-size:24px;color:#d3d6dc;transform:rotate(-90deg);transform-origin:0 0;white-space:nowrap">Starker Content</div>
    <div class="h-sm" style="left:60px;top:40px;width:118px;text-align:right;font-size:14px;font-weight:500">Jonas<br>Keller<br>&amp;<br>Marco<br>Brandt</div>
    <div class="abs" style="left:60px;top:90px;width:120px;height:1px;background:var(--line)"></div>
    <div class="abs" role="img" aria-label="Host with a child on a sports field" style="left:185px;top:42px;width:105px;height:105px;background:linear-gradient(160deg,#3a5ec8,#d8d4cc)"></div>
    <div class="abs" role="img" aria-label="Motorcycle rider on a mountain road" style="left:292px;top:42px;width:105px;height:105px;background:linear-gradient(160deg,#c9ccd0,#8a8e92 60%,#b02a2a)"></div>
    <div class="abs" style="left:399px;top:42px;width:108px;height:105px;background:var(--soft)"><svg style="position:absolute;left:40px;top:36px" width="30" height="30" viewBox="0 0 30 30"><path d="M15 2l4 8 8 1-6 6 2 9-8-4-8 4 2-9-6-6 8-1z" fill="#d3d6dc"/></svg></div>
    <div class="abs" role="img" aria-label="Red sports car seen from above" style="left:77px;top:149px;width:106px;height:105px;background:linear-gradient(160deg,#7d8086,#5a5d62)"></div>
    <div class="abs" role="img" aria-label="Waterfall in a green gorge" style="left:185px;top:149px;width:105px;height:105px;background:linear-gradient(160deg,#3e5a3a,#9ab0a8 50%,#2e3e2e)"></div>
    <div class="p-sm" style="left:305px;top:172px;width:185px;font-size:7px;line-height:1.3">«Uns ist es wichtig, dass wir Kooperationen mit Organisationen und Brands eingehen, welche zu uns passen. Wir haben über Jahre eine treue und loyale Community aufgebaut und das geht nur über guten und authentischen Content.»</div>
    <div class="footer">Your footer goes here</div><div class="pg"></div>
  </section>

  <section class="slide sm col-l r5">
    <div class="brand"><i></i>Brisk Otter</div>
    <div class="h-sm" style="left:26px;top:28px;font-size:15px">(Individuelle Folien)</div>
    <div class="p-sm" style="left:26px;top:72px;width:455px;font-size:7px;line-height:1.3">(Ideen für den Kunden)<br>Lorem ipsum dolor sit amet, consectetur adipiscing elit, sed do eiusmod tempor incididunt ut labore et dolore magna aliqua. Ut enim ad minim veniam, quis nostrud exercitation ullamco laboris nisi ut aliquip ex ea commodo consequat. Duis aute irure dolor in reprehenderit in voluptate velit esse cillum dolore eu fugiat nulla pariatur. Excepteur sint occaecat cupidatat non proident, sunt in culpa qui officia deserunt mollit anim id est laborum. Sed ut perspiciatis unde omnis iste natus error sit voluptatem accusantium doloremque laudantium, totam rem aperiam, eaque ipsa quae ab illo inventore veritatis et quasi architecto beatae vitae dicta sunt explicabo.</div>
    <div class="footer">Your footer goes here</div><div class="pg"></div>
  </section>

  <section class="slide sm col-r r5">
    <div class="brand"><i></i>Brisk Otter</div>
    <div class="h-sm" style="left:26px;top:28px;font-size:15px">Leistungen Social Media</div>
    <div class="p-sm" style="left:26px;top:58px">Social-Media Umsetzungen werden grundsätzlich wie folgt kalkuliert:</div>
    <table class="price">
      <tr><th>Post</th><th>Keller</th><th>Brandt</th><th>Keller &amp;<br>Brandt</th></tr>
      <tr><td>Stories</td><td>CHF 2'600</td><td>CHF 3'300</td><td>CHF 5'400</td></tr>
      <tr><td>Foto und einfache Videoposts</td><td>CHF 3'900</td><td>CHF 4'900</td><td>CHF 7'900</td></tr>
      <tr><td>Umfänglich e Reels</td><td>CHF 5'900</td><td>CHF 6'900</td><td>CHF 9'900</td></tr>
    </table>
    <div class="p-sm" style="left:26px;top:240px;width:190px">Zusätzliche Reichweite über Plattformen von Pulse: auf Anfrage möglich.</div>
    <div class="p-sm" style="right:26px;top:240px">Preise inkl. Kreation und Produktion, exkl. MWSt.</div>
    <div class="perk" style="top:80px"><div class="sq"><svg width="14" height="14"><circle cx="7" cy="7" r="6" fill="#fff"/><path d="M7 3l1.2 2.5 2.6.3-2 1.8.6 2.6L7 8.9 4.6 10.2l.6-2.6-2-1.8 2.6-.3z" fill="var(--navy)"/></svg></div><div class="t"><b>Branchenexklusivität:</b><br>Zuzüglich 50% des Gesamtvolumens.</div></div>
    <div class="perk" style="top:128px"><div class="sq"><svg width="14" height="14"><rect x="2" y="2" width="2" height="10" fill="#fff"/><rect x="6" y="2" width="2" height="10" fill="#fff"/><rect x="10" y="2" width="2" height="10" fill="#fff"/></svg></div><div class="t"><b>Buyouts:</b><br>50% pro Content Piece.</div></div>
    <div class="perk" style="top:176px"><div class="sq"><svg width="14" height="14"><circle cx="7" cy="7" r="6" fill="#fff"/><text x="7" y="10" text-anchor="middle" font-size="8" fill="var(--navy)" font-family="Barlow,sans-serif">%</text></svg></div><div class="t"><b>Rabatt bei Abschluss einer weiteren<br>Vereinbarung für 2024:</b><br>20% auf das Gesamtvolumen.</div></div>
    <div class="footer">Your footer goes here</div><div class="pg"></div>
  </section>

  <section class="slide sm col-l r6">
    <div class="abs" role="img" aria-label="Portrait of the contact person" style="left:26px;top:0;width:214px;height:260px;background:linear-gradient(160deg,#e8dccb,#c9b49a 55%,#8a7a66)"></div>
    <div class="brand" style="left:257px;top:86px;right:auto;font-size:10px"><i style="width:12px;height:12px"></i>Brisk Otter</div>
    <div class="h-sm" style="left:257px;top:108px;font-size:21px">Ich freue mich auf<br>die Zusammenarbeit.</div>
    <div class="abs" style="left:257px;top:168px;width:250px;height:1px;background:var(--line)"></div>
    <div class="contact" style="top:188px"><div class="c"><svg width="10" height="8"><rect x="0" y="0" width="10" height="8" rx="1" fill="var(--navy)"/><path d="M0 0l5 4 5-4" stroke="#fff" fill="none"/></svg></div><span style="color:var(--cyan);text-decoration:underline">lea@briskotter.ch</span></div>
    <div class="contact" style="top:222px"><div class="c"><svg width="10" height="10" viewBox="0 0 10 10"><path d="M2 0l2 2.5-1.2 1.4a6 6 0 0 0 3.3 3.3L7.5 6 10 8 8.5 10C4 9.5.5 6 0 1.5z" fill="var(--navy)"/></svg></div><span>+41 79 000 12 34</span></div>
  </section>

</div>
</body>
</html>
```